Redesign and move to Wordpress for quarvendo.com

Our website needs a redesign and at the same time we are moving it to Wordpress. Please help us with a new digital professional look and feel.

We are an Australian Software Engineering company specialising in advanced software development using in A.I., PLatform Engineering, Integration and Cloud. See the current quarvendo.com for more information about us.

```html
<!DOCTYPE html>
<html lang="en">
<head>
<meta charset="utf-8">
<title>Quarvendo — Reliable Smart Software Engineering</title>
<link rel="stylesheet" href="https://fonts.googleapis.com/css2?family=Work+Sans:wght@400;500;600&family=Inter:wght@400;500;600;700&display=swap">
<style>
:root{
  --navy:#0d1d4f;
  --navy-deep:#0b1a47;
  --blue:#1b5aa5;
  --teal:#4fc4bd;
  --teal-soft:#58c6bf;
  --ink:#1a2440;
  --muted:#4b5570;
  --line:#d8dfea;
  --white:#ffffff;
}
*{box-sizing:border-box;margin:0;padding:0}
html,body{width:1200px;height:3224px;overflow:hidden}
body{position:relative;background:var(--white);font-family:"Inter",sans-serif;color:var(--ink)}
.abs{position:absolute}
.heading{font-family:"Work Sans",sans-serif;font-weight:500;letter-spacing:.5px}
.btn{position:absolute;display:flex;align-items:center;justify-content:center;border-radius:16px;font-size:11px;font-weight:600}
.btn-outline{border:1.5px solid var(--blue);color:var(--blue);background:var(--white)}
.btn-teal{background:var(--teal);color:var(--white)}

/* header */
.site-header{position:absolute;left:0;top:0;width:1200px;height:62px;background:var(--white);border-bottom:1px solid #e6ebf2}
.brand{position:absolute;left:62px;top:14px;display:flex;align-items:center;gap:10px}
.brand-square{width:30px;height:30px;border:3px solid var(--blue)}
.brand-name{font-size:26px;color:var(--blue);font-weight:500;letter-spacing:1px}
.main-nav{position:absolute;top:23px;left:498px;display:flex;gap:35px;font-size:11px;color:var(--ink)}
.main-nav .active{color:var(--teal)}
.social{position:absolute;width:30px;height:30px;border:1px solid var(--teal);border-radius:50%;color:var(--teal);font-size:10px;font-weight:700;display:flex;align-items:center;justify-content:center}

/* hero */
.hero{position:absolute;left:0;top:62px;width:1200px;height:500px;background:radial-gradient(ellipse at 50% 70%,#3a73c8 0%,#24509f 45%,#16306f 100%)}
.hero-title{position:absolute;top:150px;width:1200px;text-align:center;color:var(--white);font-size:37px;line-height:50px;font-weight:600}
.partners{position:absolute;left:231px;top:515px;width:737px;height:70px;background:var(--white);border-radius:10px 10px 0 0;display:flex;justify-content:space-around;align-items:center;padding:0 70px;font-size:22px;font-weight:600;color:#2b3550}

/* welcome */
.photo{position:absolute}
.eyebrow{color:var(--teal);font-size:14px;font-weight:500}
.lead{color:var(--blue);font-size:12px;line-height:15px}
.body-copy{color:var(--muted);font-size:9px;line-height:15px}

/* services */
.services{position:absolute;left:0;top:1102px;width:1200px;height:656px;background:linear-gradient(110deg,#e7eff7 0%,#eef5f6 60%,#e4f2f1 100%)}
.svc-label{position:absolute;font-size:10.5px;line-height:13px;color:var(--ink)}

/* news */
.card-img{position:absolute;width:275px;height:187px}
.card-box{position:absolute;width:233px;height:170px;background:var(--white);padding:22px 18px}
.card-tag{position:absolute;background:var(--white);color:var(--blue);font-size:8px;font-weight:600;border-radius:10px;padding:4px 10px}
.card-date{color:var(--blue);font-size:8px;font-weight:600}
.card-title{color:var(--ink);font-size:14px;font-weight:600;line-height:19px;margin-top:14px}
.card-more{color:var(--teal);font-size:8.5px;font-weight:600;margin-top:14px}

/* promo */
.promo{position:absolute;left:0;top:2259px;width:1200px;height:437px;background:var(--teal-soft);overflow:hidden}

/* footer */
.footer{position:absolute;left:0;top:2696px;width:1200px;height:528px;background:var(--navy-deep);color:var(--white)}
.field-label{position:absolute;font-size:9px;color:#e6ebf5}
.field-line{position:absolute;height:1px;background:#5a6a95}
.foot-nav{position:absolute;top:468px;left:688px;display:flex;gap:29px;font-size:10.5px}
</style>
</head>
<body>

<header class="site-header">
  <div class="brand"><span class="brand-square"></span><span class="brand-name">quarvendo</span></div>
  <nav class="main-nav"><span class="active">Home</span><span>About us</span><span>Services</span><span>Blog</span><span>Contact us</span></nav>
  <div class="btn btn-outline" style="left:866px;top:15px;width:152px;height:31px;font-size:11px">Book an Appointment</div>
  <span class="social" style="left:1031px;top:16px">f</span>
  <span class="social" style="left:1068px;top:16px">t</span>
  <span class="social" style="left:1105px;top:16px">in</span>
</header>

<section class="hero" role="img" aria-label="Blue digital wave of glowing data particles">
  <h1 class="hero-title heading">Reliable Smart Software<br>Engineering</h1>
  <div class="btn btn-teal" style="left:534px;top:271px;width:131px;height:31px">Free Consultation</div>
</section>
<div class="partners"><span>Norvell</span><span>Brightcore</span><span>Trakline</span><span>Solvane</span></div>

<section class="welcome">
  <div class="photo" style="left:199px;top:671px;width:162px;height:110px;background:linear-gradient(135deg,#1e4d6e,#0f2b3d)" role="img" aria-label="Hand touching a digital interface"></div>
  <div class="photo" style="left:199px;top:807px;width:162px;height:220px;background:linear-gradient(160deg,#3d5c78,#0e1a28)" role="img" aria-label="Hands typing on a laptop"></div>
  <div class="photo" style="left:387px;top:671px;width:162px;height:220px;background:linear-gradient(160deg,#2a3346,#0c1220 70%,#4a3a6a)" role="img" aria-label="Developer working with data charts"></div>
  <div class="photo" style="left:387px;top:917px;width:162px;height:110px;background:linear-gradient(160deg,#c9a070,#2a2e38 50%,#101216)" role="img" aria-label="Laptop keyboard close up"></div>

  <div class="abs eyebrow" style="left:612px;top:717px">Welcome to</div>
  <h2 class="abs heading" style="left:612px;top:740px;font-size:38px;color:var(--navy)">Quarvendo</h2>
  <p class="abs lead" style="left:612px;top:808px;width:390px">We have been on a mission to <b>make complex custom enterprise integration accessible</b> to any organisation, regardless of industry, size, or location.</p>
  <p class="abs body-copy" style="left:612px;top:869px;width:380px">At Quarvendo, we craft bespoke software solutions that are not available on the market. By building organizations market-leading products, process automation, legacy system enablement, or advanced intelligent systems, we empower our customers to achieve a competitive edge in their industry.</p>
  <div class="btn btn-outline" style="left:612px;top:956px;width:107px;height:31px">Explore More</div>
</section>

<section class="services">
  <div class="abs eyebrow" style="top:76px;width:1200px;text-align:center">What we do</div>
  <h2 class="abs heading" style="top:95px;width:1200px;text-align:center;font-size:38px;color:var(--navy)">Services We Provide</h2>
  <svg class="abs" style="left:0;top:0" width="1200" height="656" viewBox="0 1102 1200 656">
    <circle cx="600" cy="1450" r="115" fill="none" stroke="var(--blue)" stroke-width="1.5" stroke-dasharray="12 10"/>
    <circle cx="600" cy="1450" r="95" fill="#fff"/>
    <text x="600" y="1457" text-anchor="middle" font-family="Inter,sans-serif" font-size="20" font-weight="500" fill="#1b5aa5">quarvendo</text>
    <g stroke-width="2" stroke-dasharray="2 4" fill="none">
      <line x1="501" y1="1342" x2="528" y2="1358" stroke="#4fc4bd"/>
      <line x1="443" y1="1413" x2="488" y2="1413" stroke="#4fc4bd"/>
      <line x1="446" y1="1494" x2="488" y2="1486" stroke="#4fc4bd"/>
      <line x1="502" y1="1564" x2="526" y2="1540" stroke="#4fc4bd"/>
      <line x1="698" y1="1340" x2="672" y2="1358" stroke="#1b5aa5"/>
      <line x1="756" y1="1413" x2="710" y2="1413" stroke="#1b5aa5"/>
      <line x1="754" y1="1494" x2="710" y2="1486" stroke="#1b5aa5"/>
      <line x1="698" y1="1564" x2="674" y2="1540" stroke="#1b5aa5"/>
    </g>
    <g fill="#4fc4bd"><circle cx="528" cy="1358" r="6"/><circle cx="490" cy="1413" r="6"/><circle cx="490" cy="1486" r="6"/><circle cx="527" cy="1540" r="6"/></g>
    <g fill="#1b5aa5"><circle cx="672" cy="1358" r="6"/><circle cx="710" cy="1413" r="6"/><circle cx="710" cy="1486" r="6"/><circle cx="674" cy="1540" r="6"/></g>
    <g fill="#fff" stroke="#4fc4bd" stroke-width="4">
      <circle cx="470" cy="1316" r="28"/><circle cx="412" cy="1409" r="28"/><circle cx="415" cy="1504" r="28"/><circle cx="474" cy="1590" r="28"/>
    </g>
    <g fill="#fff" stroke="#1b5aa5" stroke-width="4">
      <circle cx="730" cy="1316" r="28"/><circle cx="787" cy="1409" r="28"/><circle cx="785" cy="1504" r="28"/><circle cx="726" cy="1590" r="28"/>
    </g>
    <g fill="#4fc4bd"><circle cx="470" cy="1316" r="8"/><circle cx="412" cy="1409" r="8"/><circle cx="415" cy="1504" r="8"/><circle cx="474" cy="1590" r="8"/></g>
    <g fill="#1b5aa5"><circle cx="730" cy="1316" r="8"/><circle cx="787" cy="1409" r="8"/><circle cx="785" cy="1504" r="8"/><circle cx="726" cy="1590" r="8"/></g>
  </svg>
  <div class="svc-label" style="right:774px;top:201px;text-align:right">Enterprise Systems<br>Integration</div>
  <div class="svc-label" style="right:834px;top:301px;text-align:right">PLatform Engineering</div>
  <div class="svc-label" style="right:829px;top:396px;text-align:right">IPaaS</div>
  <div class="svc-label" style="right:769px;top:474px;text-align:right">Real-Time Data Stream<br>Processing</div>
  <div class="svc-label" style="left:773px;top:208px">Microservices</div>
  <div class="svc-label" style="left:830px;top:301px">Conversational AI</div>
  <div class="svc-label" style="left:828px;top:393px">Co-Agent /<br>AI Agents</div>
  <div class="svc-label" style="left:770px;top:474px">Custom Integration for Small<br>to Medium Business</div>
  <div class="btn btn-outline" style="left:447px;top:550px;width:160px;height:31px">Discover More Services</div>
  <div class="btn btn-teal" style="left:621px;top:550px;width:131px;height:31px">Free Consultation</div>
</section>

<section class="news">
  <div class="abs eyebrow" style="top:1834px;width:1200px;text-align:center">Latest Updates</div>
  <h2 class="abs heading" style="top:1853px;width:1200px;text-align:center;font-size:38px;color:var(--navy)">News &amp; Articles</h2>

  <div class="card-img" style="left:106px;top:1934px;background:linear-gradient(180deg,#1f5a2c,#3f9a4a 50%,#1a3d7a)" role="img" aria-label="Server racks lit in green and blue"></div>
  <span class="card-tag" style="left:118px;top:1946px">INTEGRATION</span>
  <article class="card-box" style="left:327px;top:1951px">
    <div class="card-date">June 24, 2024</div>
    <div class="card-title">Why most upgrade paths for FlowBridge lead to using Cirrus Flow Apps</div>
    <div class="card-more">Read More ↗</div>
  </article>

  <div class="card-img" style="left:612px;top:1934px;background:linear-gradient(135deg,#c9c4b8,#6b5f52 55%,#2e3138)" role="img" aria-label="Team meeting around a laptop with integration diagram"></div>
  <span class="card-tag" style="left:624px;top:1946px">BIZ FLOW</span>
  <article class="card-box" style="left:833px;top:1951px">
    <div class="card-date">June 24, 2024</div>
    <div class="card-title">How to get visibility into your FlowBridge environment</div>
    <div class="card-more">Read More ↗</div>
  </article>

  <div class="btn btn-outline" style="left:545px;top:2152px;width:110px;height:31px">View all News</div>
</section>

<section class="promo">
  <div class="abs" style="left:540px;top:0;width:660px;height:437px;background:linear-gradient(115deg,rgba(255,255,255,0) 30%,rgba(255,255,255,.25) 60%,rgba(200,235,232,.5))" role="img" aria-label="Abstract glass building facade lines"></div>
  <h2 class="abs heading" style="left:200px;top:97px;font-size:38px;line-height:49px;color:var(--white);font-weight:600">Australia's Largest<br>health charity implements</h2>
  <div class="abs heading" style="left:200px;top:210px;font-size:27px;color:var(--white);font-weight:600">Quarvendo API Msg Bus</div>
  <div class="abs" style="left:212px;top:281px;font-size:8.5px;color:#eef9f8">Enter your email...</div>
  <div class="abs" style="left:200px;top:295px;width:412px;height:1px;background:#d4f0ee"></div>
  <div class="btn" style="left:200px;top:311px;width:90px;height:30px;background:var(--white);color:var(--blue);border:1px solid var(--blue)">Subscribe</div>
</section>

<footer class="footer">
  <h2 class="abs heading" style="top:70px;width:1200px;text-align:center;font-size:38px;font-weight:600">How can we help you?</h2>
  <div class="abs" style="top:128px;width:1200px;text-align:center;font-size:14px;font-weight:500">Get in touch with us today!</div>

  <div class="abs" style="left:200px;top:193px;font-size:14px;font-weight:600">Contact us</div>
  <svg class="abs" style="left:200px;top:229px" width="10" height="10" viewBox="0 0 10 10"><path d="M2 1l2 2-1 1.5a6 6 0 0 0 2.5 2.5L7 6l2 2-1.5 1.5C4.5 9 1 5.5.5 2.5z" fill="#4fc4bd"/></svg>
  <div class="abs" style="left:215px;top:228px;font-size:12px">1800 555 019</div>
  <svg class="abs" style="left:200px;top:255px" width="10" height="8" viewBox="0 0 10 8"><rect x=".5" y=".5" width="9" height="7" fill="none" stroke="#4fc4bd"/><path d="M.5.5L5 4.5 9.5.5" fill="none" stroke="#4fc4bd"/></svg>
  <div class="abs" style="left:215px;top:253px;font-size:10.5px">hello@quarvendo.com</div>
  <svg class="abs" style="left:200px;top:278px" width="8" height="11" viewBox="0 0 8 11"><path d="M4 11S0 6 0 4a4 4 0 0 1 8 0c0 2-4 7-4 7z" fill="#4fc4bd"/><circle cx="4" cy="4" r="1.5" fill="#0b1a47"/></svg>
  <div class="abs" style="left:215px;top:277px;font-size:10.5px;line-height:18px">Suite 210, 8 Harbour Lane<br>Melbourne, VIC , 3004</div>

  <div class="abs" style="left:200px;top:344px;font-size:14px;font-weight:600">Follow us</div>
  <span class="social" style="left:200px;top:369px">f</span>
  <span class="social" style="left:237px;top:369px">t</span>
  <span class="social" style="left:274px;top:369px">in</span>

  <div class="field-label" style="left:461px;top:208px">Name</div>
  <div class="field-line" style="left:449px;top:230px;width:269px"></div>
  <div class="field-label" style="left:743px;top:208px">Phone</div>
  <div class="field-line" style="left:731px;top:230px;width:269px"></div>
  <div class="field-label" style="left:461px;top:258px">Email</div>
  <div class="field-line" style="left:449px;top:280px;width:551px"></div>
  <div class="field-label" style="left:461px;top:306px">Message...</div>
  <div class="field-line" style="left:449px;top:356px;width:551px"></div>
  <div class="btn btn-teal" style="left:449px;top:372px;width:75px;height:29px">Submit</div>

  <div class="abs" style="left:200px;top:470px;font-size:9px">© 2024 <span style="color:var(--teal)">quarvendo</span>. All Rights Reserved</div>
  <nav class="foot-nav"><span style="color:var(--teal)">Home</span><span>About us</span><span>Services</span><span>Blog</span><span>Contact us</span></nav>
</footer>

</body>
</html>
```